RVM Flooring Flyer/Direct Mail

I need a flyer that will be distributed by letterboxing. this flyer will be offering free measure and quotes for supply and installation of timber, bamboo, and laminate flooring. The flyer will need to eye catching and professional looking.
The main purpose of the flyer is to generate appointments that will be followed up by a sales measure and quote team.

- Free Measure and Quote
Services:
- Remove and dispose of old floor coverings
- Pre installation floor repair
- New floor installation
- Free dust and clean on every new floor installation

I have some design files, logo and stock images, the flyer must not clash with the logo and business card.

You can use any image from Pextra Images as I have subscription with them.
https://images.pextrafoto.com/au/gallery

Here are the links to the Timber and Bamboo flooring supplier that I will be buying from and the third link is for the laminate flooring supplier. Note, this is for getting an idea of what products we will be supplying and installing, Do not use their images!

https://www.grainhaven.com.au/timber-flooring/
https://cantorvex.com.au/bamboo-flooring/
http://www.dalvorsurfaces.com.au/brands/tenmark-laminate/

Target Market(s)

Domestic home owners

Industry/Entity Type

Construction Company

Colors

Designer to choose colors to be used in the design.

Requirements
Must have
• Size: A6 or DL
Nice to have
• Timber: Spotted Gum, Eastern States Blackbutt, Jarrah, Marri, and a large collection of French Oak.
• Bamboo: Our Bamboo range of flooring is engineered to withstand the extremes of the Australian climate.
• Laminate: All our laminate range comes with a 25 year product warranty. Choose from a large range of patterns, colours and finishes.

```html
<!DOCTYPE html>
<html lang="en">
<head>
<meta charset="utf-8">
<title>RVM Flooring – Free Measure &amp; Quote Flyer</title>
<link href="https://fonts.googleapis.com/css2?family=Cinzel:wght@400;600&family=Crimson+Text:wght@400;600;700&family=Montserrat:wght@500&display=swap" rel="stylesheet">
<style>
  :root{
    --bg:#e6e7ea;
    --slate:#46566b;
    --slate-dark:#34404f;
    --mist:#aeb9c7;
    --mist-light:#d5dbe3;
    --paper:#ffffff;
    --paper-tint:#f1f2f4;
    --ink:#2e3339;
    --ink-soft:#4b5159;
  }
  *{margin:0;padding:0;box-sizing:border-box}
  html,body{width:1200px;height:983px;overflow:hidden;background:var(--bg)}
  .flyer{
    position:absolute;left:275px;top:32px;width:650px;height:920px;
    background:linear-gradient(180deg,var(--paper) 30%,var(--paper-tint) 100%);
    box-shadow:0 6px 24px rgba(0,0,0,.18);overflow:hidden;
    font-family:"Crimson Text",Georgia,serif;color:var(--ink);
  }
  .shapes,.photo{position:absolute;left:0;top:0}
  .brand{
    position:absolute;left:0;top:0;width:190px;height:270px;
    display:flex;flex-direction:column;align-items:center;justify-content:center;gap:18px;
  }
  .brand-mark{width:46px;height:46px;border:3px solid #fff}
  .brand-name{font-family:"Montserrat",Arial,sans-serif;font-weight:500;color:#fff;font-size:19px;letter-spacing:.5px}
  .headline{position:absolute;left:38px;top:300px;color:var(--slate)}
  .headline-free{font-family:"Cinzel",serif;font-size:88px;line-height:1;font-weight:400}
  .headline-sub{font-family:"Crimson Text",serif;font-size:36px;font-weight:600;margin:-2px 0 0 40px;line-height:1}
  .intro{position:absolute;left:38px;top:438px;width:380px;font-size:15px;line-height:1.25;color:var(--ink-soft);text-align:justify}
  .services-tab{
    position:absolute;left:38px;top:590px;width:200px;height:38px;
    background:var(--slate);color:#fff;font-size:23px;line-height:1;
    clip-path:polygon(0 0,100% 0,92% 100%,0 100%);
    padding:7px 0 0 22px;
  }
  .services-list{position:absolute;left:44px;top:638px;list-style:none;font-size:16px;color:var(--ink-soft)}
  .services-list li{display:flex;align-items:center;gap:10px;height:28px}
  .services-list svg{flex:none}
  .cta{position:absolute;left:44px;top:760px}
  .cta-title{font-family:"Cinzel",serif;font-size:26px;line-height:1.1;color:var(--slate)}
  .cta-note{font-size:15px;color:var(--ink-soft);margin-top:2px}
  .phones{position:absolute;left:44px;top:818px;font-size:23px;font-weight:700;color:var(--ink);line-height:1.3}
  .contact-line{display:flex;align-items:center;gap:8px}
  .details{position:absolute;left:256px;top:824px;font-size:14px;font-weight:600;color:var(--ink);line-height:1.7}
</style>
</head>
<body>
<div class="flyer">
  <svg class="shapes" width="650" height="920" viewBox="0 0 650 920" aria-hidden="true">
    <defs>
      <linearGradient id="panelTone" x1="0" y1="0" x2="0" y2="1">
        <stop offset="0" stop-color="#56667b"/><stop offset="1" stop-color="#3a4757"/>
      </linearGradient>
    </defs>
    <rect x="0" y="0" width="190" height="270" fill="url(#panelTone)"/>
    <polygon points="0,270 440,256 650,196 650,262 470,282 0,282" fill="var(--mist)"/>
    <polygon points="0,282 470,282 650,262 650,276 0,290" fill="var(--mist-light)"/>
    <polygon points="0,888 650,842 650,920 0,920" fill="var(--mist-light)"/>
    <polygon points="0,904 650,866 650,920 0,920" fill="var(--mist)"/>
    <polygon points="548,268 630,350 548,432 466,350" fill="var(--slate-dark)"/>
    <polygon points="568,404 646,482 568,560 490,482" fill="var(--slate-dark)"/>
    <polygon points="568,540 646,618 568,696 490,618" fill="var(--slate-dark)"/>
  </svg>

  <svg class="photo" width="650" height="270" viewBox="0 0 650 270" role="img" aria-label="Photo of a bright modern dining room with fireplace, pendant lights and light timber floor">
    <defs><linearGradient id="roomTone" x1="0" y1="0" x2="1" y2="1">
      <stop offset="0" stop-color="#c9ccd0"/><stop offset=".6" stop-color="#a7abb1"/><stop offset="1" stop-color="#8c8f94"/>
    </linearGradient></defs>
    <polygon points="190,0 650,0 650,196 440,256 190,262" fill="url(#roomTone)"/>
  </svg>

  <svg class="photo" width="650" height="920" viewBox="0 0 650 920" role="img" aria-label="Photo of timber, bamboo and laminate flooring sample boards">
    <defs><linearGradient id="sampleTone" x1="0" y1="0" x2="1" y2="1">
      <stop offset="0" stop-color="#8a6a4c"/><stop offset=".5" stop-color="#b9a58a"/><stop offset="1" stop-color="#5e5550"/>
    </linearGradient></defs>
    <polygon points="540,262 618,340 540,418 462,340" fill="url(#sampleTone)"/>
  </svg>

  <svg class="photo" width="650" height="920" viewBox="0 0 650 920" role="img" aria-label="Photo of an open living space with polished timber floor">
    <defs><linearGradient id="livingTone" x1="0" y1="0" x2="0" y2="1">
      <stop offset="0" stop-color="#e4e6e8"/><stop offset=".55" stop-color="#c8c3bb"/><stop offset="1" stop-color="#8e6f4f"/>
    </linearGradient></defs>
    <polygon points="560,400 634,474 560,548 486,474" fill="url(#livingTone)"/>
  </svg>

  <svg class="photo" width="650" height="920" viewBox="0 0 650 920" role="img" aria-label="Close-up photo of timber floorboards">
    <defs><linearGradient id="boardTone" x1="0" y1="0" x2="1" y2="1">
      <stop offset="0" stop-color="#a88a5e"/><stop offset=".5" stop-color="#7d5f3c"/><stop offset="1" stop-color="#4f3b26"/>
    </linearGradient></defs>
    <polygon points="560,536 634,610 560,684 486,610" fill="url(#boardTone)"/>
  </svg>

  <div class="brand">
    <span class="brand-mark"></span>
    <span class="brand-name">RVM FLOORING</span>
  </div>

  <div class="headline">
    <div class="headline-free">FREE</div>
    <div class="headline-sub">Measure &amp; Quote</div>
  </div>

  <p class="intro">At RVM flooring we specialise in prefinished timber, bamboo and laminate flooring. We strive to provide a unique and professional experience to all our customers. Our goal is to provide the highest standard in customer service, integrity, quality and value for money. As a family business we understand the importance of relationship and seek to make your experience one you will be pleased you made.</p>

  <div class="services-tab">Services</div>
  <ul class="services-list">
    <li><svg width="14" height="14" viewBox="0 0 14 14"><rect x="1" y="1" width="12" height="12" fill="none" stroke="var(--slate)" stroke-width="2"/><path d="M1 7h12M7 1v12" stroke="var(--slate)" stroke-width="1.5"/></svg>Remove &amp; dispose of old floor coverings</li>
    <li><svg width="14" height="14" viewBox="0 0 14 14"><circle cx="7" cy="7" r="5" fill="none" stroke="var(--slate)" stroke-width="3" stroke-dasharray="2 1.6"/><circle cx="7" cy="7" r="2" fill="var(--slate)"/></svg>Pre installation floor repair</li>
    <li><svg width="14" height="14" viewBox="0 0 14 14"><circle cx="5" cy="4" r="2.5" fill="var(--slate)"/><circle cx="10" cy="5" r="2" fill="var(--slate)"/><path d="M0 13c0-4 10-4 10 0zM8 13c0-3 6-3 6 0z" fill="var(--slate)"/></svg>New floor installation</li>
    <li><svg width="14" height="14" viewBox="0 0 14 14"><path d="M11 1L6 8" stroke="var(--slate)" stroke-width="1.6"/><path d="M5 7l3 2-3 4-3-1z" fill="var(--slate)"/></svg>Free dust and clean on every new floor installation</li>
  </ul>

  <div class="cta">
    <div class="cta-title">CALL TODAY</div>
    <div class="cta-note">For your obligations free quote &amp; to view our range of products.</div>
  </div>

  <div class="phones">
    <div class="contact-line"><svg width="20" height="16" viewBox="0 0 20 16"><path d="M1 5c0-4 18-4 18 0v2h-5V5H6v2H1z" fill="var(--ink)"/><rect x="4" y="8" width="12" height="7" rx="1" fill="var(--ink)"/></svg>0491 570 006</div>
    <div class="contact-line"><svg width="20" height="16" viewBox="0 0 20 16"><path d="M1 5c0-4 18-4 18 0v2h-5V5H6v2H1z" fill="var(--ink)"/><rect x="4" y="8" width="12" height="7" rx="1" fill="var(--ink)"/></svg>08 5550 1234</div>
  </div>

  <div class="details">
    <div class="contact-line"><svg width="18" height="13" viewBox="0 0 18 13"><rect x="1" y="1" width="16" height="11" fill="none" stroke="var(--slate)" stroke-width="2"/><path d="M1 1l8 6 8-6" fill="none" stroke="var(--slate)" stroke-width="2"/></svg>sam@rvmflooring.example</div>
    <div class="contact-line"><svg width="12" height="16" viewBox="0 0 12 16"><path d="M6 0a6 6 0 0 1 6 6c0 4-6 10-6 10S0 10 0 6a6 6 0 0 1 6-6z" fill="var(--slate)"/><circle cx="6" cy="6" r="2.2" fill="#fff"/></svg>12 Sample Parade, Wattlegrove North WA 6999</div>
  </div>
</div>
</body>
</html>
```